Website design and coding for new consultancy company

I need to have a full website designed for a new consultancy business I'm trying to establish. It's called Brightpath consult. I need an English version to begin with, and then there should be a Danish version as well, but I'll translate that myself. Just be aware that I need two language versions. The consultancy field that I'm targeting is Leadership - and specialist development. I offer to facilitate corporate academies for global companies as well as specific workshops within leadership- or team development, strategy sessions, personal coaching and facilitation of D&I (Diversity and inclusion) workshops. BTW my logo is not in high resolution - I need that as well.

Target Market(s)

Larger companies that has a need for developing their inhouse leadership capabilities or that wants to develop their specialists to take on more responsibility.

Industry/Entity Type

Consultancy business

Coding

Number of Pages Required

5+ page

Requirements
Must have
• Introduction site with a catch phrase. Book a meeting. Services that's beeing offered. Blog site with white papers etc. Language toggle (Danish/English). Cases/testimonials. About site. Contact site.

```html
<!DOCTYPE html>
<html lang="en">
<head>
<meta charset="utf-8">
<title>Brightpath Consult</title>
<link href="https://fonts.googleapis.com/css2?family=Poppins:ital,wght@0,400;0,500;0,600;1,400&display=swap" rel="stylesheet">
<style>
:root{
  --blue:#1f7ad6;
  --blue-dark:#1565c0;
  --ink:#2b2b2b;
  --muted:#6b6b6b;
  --accent:#e8462b;
  --band:#f5f3f4;
  --footer:#2f2f33;
  --careers:#e6ecf3;
}
*{box-sizing:border-box;margin:0;padding:0}
html,body{width:1200px;height:3409px;overflow:hidden}
body{font-family:'Poppins',sans-serif;color:var(--ink);background:#fff;position:relative}
.abs{position:absolute}
.ph{position:absolute}
.btn{position:absolute;background:var(--blue);color:#fff;font-size:10.5px;font-weight:500;display:flex;align-items:center;justify-content:center;border-radius:2px}
.eyebrow{position:absolute;left:0;width:1200px;text-align:center;font-size:10px;color:var(--blue);text-transform:uppercase;letter-spacing:.2px}
.section-title{position:absolute;left:0;width:1200px;text-align:center;font-size:26px;font-weight:500;color:#333}

/* hero */
.hero{position:absolute;left:0;top:0;width:1200px;height:524px;background:linear-gradient(100deg,#1b1f26 0%,#3a434e 45%,#59636e 70%,#2a3440 100%);overflow:hidden}
.hero-shade{position:absolute;inset:0;background:linear-gradient(90deg,rgba(10,14,20,.55),rgba(10,14,20,.1) 70%)}
.brand{position:absolute;display:flex;align-items:center;gap:9px;color:#fff;font-weight:600;white-space:nowrap}
.brand .mark{width:28px;height:28px;border:2px solid var(--blue);border-radius:50%;flex:none}
.nav{position:absolute;top:41px;font-size:10.5px;color:#fff;white-space:nowrap}
.lang-toggle{position:absolute;left:982px;top:36px;height:23px;display:flex;border:1px solid rgba(255,255,255,.6);border-radius:12px;overflow:hidden;font-size:9.5px;font-weight:500}
.lang-toggle span{width:30px;display:flex;align-items:center;justify-content:center;color:#fff}
.lang-toggle .active{background:var(--blue)}
.hero-title{position:absolute;left:234px;top:220px;font-size:39px;font-weight:600;color:#fff;letter-spacing:-.3px;white-space:nowrap}
.hero-sub{position:absolute;left:234px;top:277px;width:470px;font-size:12.5px;line-height:15px;color:#fff}
.slider-arrow{position:absolute;width:36px;height:36px;border-radius:50%;display:flex;align-items:center;justify-content:center}

/* about */
.about-text{position:absolute;left:628px;width:340px}
.about-text p{font-size:10.5px;line-height:16px;color:var(--muted)}

/* process */
.step{position:absolute;width:180px;text-align:center;top:1104px}
.step h4{font-size:14px;font-weight:500;color:#333}
.step .sub{font-size:9.5px;color:var(--muted);margin-top:2px}
.step .icon{position:relative;margin:17px auto 0;width:44px;height:44px;background:#2d6fd2;border-radius:3px;display:flex;align-items:center;justify-content:center}
.step .num{position:absolute;right:-10px;top:13px;width:18px;height:18px;border-radius:50%;background:#fff;border:1px solid #ddd;font-size:8px;display:flex;align-items:center;justify-content:center;color:#333}
.step .desc{font-size:10px;line-height:17px;color:#555;margin-top:18px}

/* services */
.services{position:absolute;left:0;top:1290px;width:1200px;height:714px;background:var(--band)}
.service-caption{position:absolute;font-size:16px;font-weight:500;color:#333;white-space:nowrap}

/* team */
.member-name{position:absolute;background:#fff;text-align:center;box-shadow:0 4px 12px rgba(0,0,0,.08);padding-top:12px}
.member-name b{display:block;font-size:11.5px;font-weight:600;color:#222}
.member-name span{font-size:8.5px;color:#888}

/* testimonials */
.review{position:absolute;top:2532px;width:429px;height:195px;border:1px solid #e4e4e4;border-radius:8px;background:#fff}
.review .avatar{position:absolute;left:16px;top:36px;width:50px;height:50px;border-radius:50%}
.review .sign{position:absolute;left:82px;top:34px;width:62px;height:22px;background:linear-gradient(90deg,#d9d9d9,#efefef);border-radius:2px}
.review .stars{position:absolute;left:175px;top:33px;color:var(--blue);font-size:16px;letter-spacing:1px}
.review .quote{position:absolute;right:22px;top:8px;font-size:80px;font-weight:600;color:#e6e6e6;line-height:1}
.review .who{position:absolute;left:82px;top:71px;font-size:11.5px;color:#444}
.review .who b{color:var(--blue);font-weight:600}
.review p{position:absolute;left:82px;top:94px;width:325px;font-size:10.5px;line-height:18.5px;font-style:italic;color:#666}

/* careers */
.careers{position:absolute;left:165px;top:2829px;width:868px;height:284px;border-radius:14px;overflow:hidden;background:var(--careers)}

/* footer */
.footer{position:absolute;left:0;top:3176px;width:1200px;height:233px;background:var(--footer);color:#fff}
.footer .link{position:absolute;font-size:10.5px;color:#eee}
.footer small{position:absolute;font-size:8.5px;color:#ccc}
</style>
</head>
<body>

<!-- HERO -->
<section class="hero">
  <div class="ph" role="img" aria-label="Smiling businessman shaking hands with a colleague in a bright office" style="left:420px;top:0;width:780px;height:524px;background:radial-gradient(ellipse at 40% 30%,rgba(190,200,210,.35),rgba(0,0,0,0) 60%)"></div>
  <div class="hero-shade"></div>
  <svg class="abs" style="left:0;top:0" width="1200" height="524" viewBox="0 0 1200 524">
    <polygon points="1075,0 1160,0 760,524 660,524" fill="#2c7fe0" opacity=".55"/>
    <polygon points="720,400 1000,524 660,524" fill="#1f7ad6" opacity=".95"/>
  </svg>
  <div class="brand" style="left:234px;top:33px;font-size:22px;letter-spacing:.3px"><span class="mark"></span>BRIGHTPATH</div>
  <div class="nav" style="left:459px">Home</div>
  <div class="nav" style="left:515px">About Us</div>
  <div class="nav" style="left:586px">Services</div>
  <div class="nav" style="left:654px">Careers</div>
  <div class="nav" style="left:713px">Blog</div>
  <div class="nav" style="left:761px">Contact Us</div>
  <div class="btn" style="left:853px;top:33px;width:113px;height:29px">Appointment &nbsp;›</div>
  <div class="lang-toggle" aria-label="Language"><span class="active">EN</span><span>DA</span></div>
  <h1 class="hero-title">Brightpath Consult Ltd</h1>
  <p class="hero-sub">Corporate Academies I Leadership Development I Team Workshops I Strategy Sessions I Personal Coaching I D&amp;I Workshops.</p>
  <div class="btn" style="left:234px;top:324px;width:101px;height:29px">Learn More</div>
  <div class="slider-arrow" style="left:51px;top:248px"><svg width="12" height="16"><path d="M9 1 2 8l7 7" stroke="#fff" stroke-width="1.5" fill="none"/></svg></div>
  <div class="slider-arrow" style="left:1113px;top:248px;background:rgba(60,70,80,.8)"><svg width="12" height="16"><path d="M3 1l7 7-7 7" stroke="#fff" stroke-width="1.5" fill="none"/></svg></div>
</section>

<!-- ABOUT -->
<div class="ph" role="img" aria-label="Team meeting around an office table" style="left:234px;top:623px;width:156px;height:306px;background:linear-gradient(160deg,#6f6a63,#2e2b29)"></div>
<div class="ph" role="img" aria-label="Portrait of a smiling bearded consultant" style="left:390px;top:586px;width:182px;height:263px;background:linear-gradient(160deg,#e9e9e7,#b9b3ac)"></div>
<div class="ph" role="img" aria-label="Group of colleagues celebrating together" style="left:347px;top:786px;width:187px;height:180px;background:linear-gradient(160deg,#5c6670,#2b3036);border:2px solid #fff"></div>
<div class="about-text" style="top:630px">
  <div style="font-size:10px;color:var(--blue)">ABOUT COMPANY</div>
  <h2 style="font-size:26px;font-weight:500;line-height:31px;color:#333;margin-top:8px">Creating A Business With<br>Authentic Integrity</h2>
  <p style="margin-top:19px">Our power of choices is untrammelled and when nothing prevents to do what we like best principle of selection.</p>
  <div style="font-size:13px;font-weight:500;color:var(--accent);margin-top:18px">Client Focused</div>
  <p style="margin-top:12px">Every pleasures is to welcomed pain avoided owing to the duty the obligations of business it will frequently occur that pleasures have be repudiated and annoyances accepted.</p>
</div>
<div class="btn" style="left:628px;top:884px;width:101px;height:31px">Learn More</div>

<!-- WORK PROCESS -->
<div class="eyebrow" style="top:1025px">Work Process</div>
<div class="section-title" style="top:1039px">Way To Reach Success</div>
<div class="abs" style="left:315px;top:1172px;width:562px;height:1px;background:#e5e5e5"></div>
<div class="step" style="left:225px">
  <h4>Contract</h4><div class="sub">First step of process</div>
  <div class="icon"><svg width="22" height="22" fill="none" stroke="#fff" stroke-width="1.5"><rect x="4" y="2" width="12" height="17"/><path d="M7 7h6M7 11h6M7 15h3"/></svg><span class="num">01</span></div>
  <div class="desc">Equal blame belongs to those<br>who fail in their duty.</div>
</div>
<div class="step" style="left:411px">
  <h4>Discussion</h4><div class="sub">Our second easy step</div>
  <div class="icon"><svg width="22" height="22" fill="none" stroke="#fff" stroke-width="1.5"><circle cx="11" cy="11" r="8"/><circle cx="11" cy="11" r="3"/><path d="M11 1v5M11 16v5M1 11h5M16 11h5"/></svg><span class="num">02</span></div>
  <div class="desc">Indignation &amp; dislike men who are<br>so beguiled.</div>
</div>
<div class="step" style="left:599px">
  <h4>Implement</h4><div class="sub">Important third step</div>
  <div class="icon"><svg width="22" height="22" fill="none" stroke="#fff" stroke-width="1.5"><path d="M11 2c4 3 5 8 3 14H8C6 10 7 5 11 2z"/><path d="M8 16l-3 4M14 16l3 4"/><circle cx="11" cy="9" r="2"/></svg><span class="num">03</span></div>
  <div class="desc">Have to repudiated accepted wise<br>always holds.</div>
</div>
<div class="step" style="left:787px">
  <h4>Closure</h4><div class="sub">Solution in final step</div>
  <div class="icon"><svg width="22" height="22" fill="none" stroke="#fff" stroke-width="1.5"><path d="M2 19l7-12 4 6 2-3 5 9z"/><path d="M9 3v4"/></svg><span class="num">04</span></div>
  <div class="desc">Desire, that they cannot foresee<br>the pain and bound.</div>
</div>

<!-- SERVICES -->
<section class="services"></section>
<div class="eyebrow" style="top:1325px">What We Do</div>
<div class="section-title" style="top:1340px">Consulting Services</div>
<div class="ph" role="img" aria-label="Facilitator presenting charts to a workshop group" style="left:234px;top:1412px;width:348px;height:182px;background:linear-gradient(120deg,#c9ccd2,#3b3a3c 55%,#1e1d1f)"></div>
<div class="ph" role="img" aria-label="Two specialists in suits reviewing a tablet" style="left:617px;top:1412px;width:347px;height:182px;background:linear-gradient(120deg,#d6d7d5,#6c727a 60%,#3c424a)"></div>
<div class="service-caption" style="left:233px;top:1610px">Corporate Academies</div>
<div class="service-caption" style="left:616px;top:1610px">Specialist Development</div>
<div class="ph" role="img" aria-label="Team working on laptops around a long desk" style="left:234px;top:1670px;width:348px;height:182px;background:linear-gradient(120deg,#6a6560,#bdb7af 55%,#8c8782)"></div>
<div class="ph" role="img" aria-label="Business team collaborating around a table" style="left:617px;top:1670px;width:347px;height:182px;background:linear-gradient(120deg,#dcdde0,#8f959c 55%,#43494f)"></div>
<div class="service-caption" style="left:233px;top:1868px">Strategy Sessions &amp; Coaching</div>
<div class="service-caption" style="left:616px;top:1868px">Team &amp; D&amp;I Workshops</div>
<div class="btn" style="left:550px;top:1936px;width:100px;height:31px">View All</div>

<!-- TEAM -->
<div class="eyebrow" style="top:2054px">Our Team</div>
<div class="section-title" style="top:2068px">Professional Team Members</div>
<div class="ph" role="img" aria-label="Portrait of team member in sunglasses" style="left:234px;top:2145px;width:169px;height:223px;background:linear-gradient(160deg,#c8cdd2,#3b4049)"></div>
<div class="ph" role="img" aria-label="Portrait of team member with glasses" style="left:422px;top:2145px;width:168px;height:223px;background:linear-gradient(160deg,#b9a9c6,#2f3037)"></div>
<div class="ph" role="img" aria-label="Portrait of team member in blue suit" style="left:609px;top:2145px;width:169px;height:223px;background:linear-gradient(160deg,#f0f0f0,#4e5866)"></div>
<div class="ph" role="img" aria-label="Portrait of team member outdoors" style="left:796px;top:2145px;width:170px;height:223px;background:linear-gradient(160deg,#dfe3e8,#525a63)"></div>
<div class="member-name" style="left:253px;top:2343px;width:131px;height:60px"><b>Clara Holm</b><span>Founder &amp; CEO</span></div>
<div class="member-name" style="left:441px;top:2343px;width:131px;height:60px"><b>Peter Lind</b><span>Regional Leader</span></div>
<div class="member-name" style="left:628px;top:2343px;width:131px;height:60px"><b>Jonas Berg</b><span>Managing Partner</span></div>
<div class="member-name" style="left:815px;top:2343px;width:131px;height:60px"><b>Martin Dahl</b><span>Chief Executive</span></div>

<!-- CASE STUDIES -->
<div class="eyebrow" style="top:2453px">Latest Articles</div>
<div class="section-title" style="top:2468px">Case Studies &amp; Success Stories</div>
<svg class="abs" style="left:141px;top:2622px" width="12" height="16"><path d="M9 1 2 8l7 7" stroke="#777" stroke-width="1.3" fill="none"/></svg>
<svg class="abs" style="left:1045px;top:2622px" width="12" height="16"><path d="M3 1l7 7-7 7" stroke="#777" stroke-width="1.3" fill="none"/></svg>
<div class="review" style="left:164px">
  <div class="avatar" role="img" aria-label="Client portrait" style="background:linear-gradient(160deg,#9aa3ad,#3a3f47)"></div>
  <div class="sign" role="img" aria-label="Handwritten signature"></div>
  <div class="stars">★★★★★</div>
  <div class="quote">”</div>
  <div class="who">Oliver Grant – <b>Broker Partner</b></div>
  <p>Sofie is one of a kind. She has been a key partner to our business and has run the extra mile to ensure our clients are looked after. I highly recommend her for any non-conforming lending scenarios.</p>
</div>
<div class="review" style="left:605px">
  <div class="avatar" role="img" aria-label="Client portrait" style="background:linear-gradient(160deg,#c4b8a8,#4a4038)"></div>
  <div class="sign" role="img" aria-label="Handwritten signature"></div>
  <div class="stars">★★★★★</div>
  <div class="quote">”</div>
  <div class="who">Oliver Grant – <b>Broker Partner</b></div>
  <p>Sofie is one of a kind. She has been a key partner to our business and has run the extra mile to ensure our clients are looked after. I highly recommend her for any non-conforming lending scenarios.</p>
</div>
<svg class="abs" style="left:574px;top:2758px" width="52" height="8">
  <circle cx="4" cy="4" r="2.6" fill="#b9c6d6"/><circle cx="13" cy="4" r="2.6" fill="#b9c6d6"/><circle cx="22" cy="4" r="2.6" fill="#b9c6d6"/><rect x="29" y="1.2" width="19" height="5.6" rx="2.8" fill="#1f7ad6"/>
</svg>

<!-- CAREERS -->
<section class="careers">
  <div class="ph" role="img" aria-label="Professional holding a tablet in front of glowing data charts" style="left:434px;top:0;width:434px;height:284px;background:linear-gradient(135deg,#1b4f7e,#2a78b5 45%,#0f2f52)"></div>
  <h2 class="abs" style="left:48px;top:50px;font-size:26px;font-weight:500;color:#333">Careers &amp; Hiring</h2>
  <p class="abs" style="left:48px;top:96px;width:340px;font-size:9.6px;line-height:15.6px;color:#555">At Northvale we are a primarily remote company. This allows our employees to work from home, whilst trying to achieve our Net Zero emissions goal by 2050. Our culture has been critical to our success, allowing us to attract and retain outstanding employees, making work here more enjoyable. We are also proud to be an equal opportunity employer.</p>
  <div class="btn" style="left:48px;top:201px;width:99px;height:30px">Apply Now</div>
</section>

<!-- FOOTER -->
<footer class="footer">
  <div class="brand" style="left:234px;top:60px;font-size:28px"><span class="mark" style="width:32px;height:32px"></span>BRIGHTPATH</div>
  <p class="abs" style="left:234px;top:119px;width:290px;font-size:9.5px;line-height:13.5px;color:#ddd">Best a to first of to chooses that was pattern. From to have highly epic either she hopes forth. Ourselves, effects That in thin because derived just then the they queen, one people away, then into the my the or big and in break.</p>
  <div class="link" style="left:574px;top:60px">Home</div>
  <div class="link" style="left:642px;top:60px">Team</div>
  <div class="link" style="left:574px;top:97px">About Us</div>
  <div class="link" style="left:642px;top:97px">Careers</div>
  <div class="link" style="left:574px;top:135px">Services</div>
  <div class="link" style="left:642px;top:135px">Contacts</div>
  <small style="left:745px;top:52px">Have Any Question?</small>
  <div class="abs" style="left:745px;top:65px;font-size:17px;color:#fff">07000 555 218</div>
  <small style="left:745px;top:99px">Our Mailbox</small>
  <div class="abs" style="left:745px;top:112px;font-size:15px;color:#fff">hello@brightpath-consult.example</div>
  <div class="abs" style="left:745px;top:148px;width:220px;height:1px;background:#55555b"></div>
  <small style="left:745px;top:166px">Social Links</small>
  <span class="abs" style="left:747px;top:187px;width:9px;height:9px;border-radius:50%;background:#fff"></span>
  <span class="abs" style="left:777px;top:187px;width:9px;height:9px;border-radius:50%;background:#fff"></span>
</footer>

</body>
</html>
```